Corvenix Business Card

Our mission is to craft high value solutions combining consulting and edge technologies for helping big and middle sized companies in the Digital Transformation Process that they must face. We think that this transformation will impact business processes and people skills in a new manner. Corvenix's value proposition is to collaborate with our clients for creating new competitive advantages based on technology, processes and people.
We already have a logo designed through your platform.

Industry/Entity Type

Business

```html
<!DOCTYPE html>
<html lang="en">
<head>
<meta charset="UTF-8">
<title>Corvenix Business Card</title>
<link href="https://fonts.googleapis.com/css2?family=Open+Sans:wght@400;600&display=swap" rel="stylesheet">
<style>
  :root {
    --page: #e9eaec;
    --card: #ffffff;
    --ink: #3a3d42;
    --muted: #6b6f75;
    --accent: #1f93d6;
    --divider: #9a9da2;
  }
  * { margin: 0; padding: 0; box-sizing: border-box; }
  html, body { width: 1200px; height: 911px; overflow: hidden; }
  body {
    background: var(--page);
    font-family: "Open Sans", Arial, sans-serif;
    color: var(--ink);
    display: flex;
    flex-direction: column;
    align-items: center;
    justify-content: center;
    gap: 40px;
  }
  .card {
    position: relative;
    width: 700px;
    height: 400px;
    background: var(--card);
    border-radius: 22px;
    box-shadow: 0 6px 18px rgba(0,0,0,0.12);
    overflow: hidden;
  }
  .rule {
    position: absolute;
    left: 0; right: 0;
    top: 250px;
    height: 5px;
    background: var(--accent);
  }
  .rule::after {
    content: "";
    position: absolute;
    left: 50%;
    top: 50%;
    width: 18px; height: 18px;
    background: var(--accent);
    transform: translate(-50%, -50%);
  }
  .brand {
    position: absolute;
    display: flex;
    align-items: center;
    gap: 14px;
  }
  .brand-mark {
    width: 50px; height: 50px;
    border-radius: 50%;
    background: var(--accent);
  }
  .brand-name {
    font-weight: 400;
    font-size: 40px;
    letter-spacing: 2px;
    color: var(--ink);
  }
  .card--back .brand { left: 50%; top: 130px; transform: translateX(-50%); }
  .card--front .brand { left: 44px; top: 110px; }
  .card--front .brand-name { font-size: 36px; }
  .divider {
    position: absolute;
    left: 420px;
    top: 60px;
    width: 3px;
    height: 170px;
    background: var(--divider);
  }
  .person {
    position: absolute;
    left: 440px;
    top: 56px;
  }
  .person-name {
    font-weight: 600;
    font-size: 20px;
    color: var(--accent);
    letter-spacing: 0.5px;
  }
  .person-role { font-size: 17px; color: var(--muted); }
  .contacts {
    position: absolute;
    left: 413px;
    top: 128px;
    list-style: none;
  }
  .contacts li {
    display: flex;
    align-items: center;
    gap: 14px;
    height: 26px;
    font-size: 15px;
    color: var(--ink);
  }
  .contacts li::before {
    content: "";
    width: 17px; height: 12px;
    background: var(--accent);
    flex: none;
  }
  .address {
    position: absolute;
    left: 44px;
    top: 290px;
    font-size: 20px;
    color: var(--ink);
  }
</style>
</head>
<body>
  <section class="card card--back">
    <div class="brand">
      <span class="brand-mark"></span>
      <span class="brand-name">CORVENIX</span>
    </div>
    <div class="rule"></div>
  </section>

  <section class="card card--front">
    <div class="brand">
      <span class="brand-mark"></span>
      <span class="brand-name">CORVENIX</span>
    </div>
    <div class="divider"></div>
    <div class="person">
      <p class="person-name">DANIEL HARTWELL</p>
      <p class="person-role">Managing Director</p>
    </div>
    <ul class="contacts">
      <li>014 782 3056</li>
      <li>014 782 3057</li>
      <li>hello@corvenix.com</li>
      <li>corvenix.com</li>
    </ul>
    <div class="rule"></div>
    <p class="address">Halvern, Ostry 118 Linden St. Marlow</p>
  </section>
</body>
</html>
```